Copperleaf Motorized Shade Business Card

Hello, we've had our logo made. Now we are looking for a clean and cool looking business card. One side can just be the logo with any design elements that might look good with it. The other side will be Name, Phone Number and Email. There will not be an address on the card.

```html
<!DOCTYPE html>
<html lang="en">
<head>
<meta charset="UTF-8">
<title>Copperleaf Motorized Shade – Business Card</title>
<link rel="stylesheet" href="https://fonts.googleapis.com/css2?family=Oswald:wght@500;600&family=Nunito+Sans:wght@400;600&display=swap">
<style>
  :root {
    --backdrop: #1d1e21;
    --navy: #17326b;
    --sky: #2aa1d9;
    --silver: #dde1e6;
    --white: #f4f6f9;
    --gold: #f2b01e;
  }
  * { margin: 0; padding: 0; box-sizing: border-box; }
  html, body {
    width: 1200px;
    height: 900px;
    overflow: hidden;
    background: var(--backdrop);
  }
  .sheet {
    width: 1200px;
    height: 900px;
    display: flex;
    flex-direction: column;
    align-items: center;
    justify-content: center;
    gap: 44px;
  }
  .card {
    position: relative;
    width: 560px;
    height: 320px;
    background: var(--navy);
    overflow: hidden;
    box-shadow: 0 14px 30px rgba(0, 0, 0, 0.45);
  }
  .card-front .bands {
    position: absolute;
    inset: 0;
    width: 100%;
    height: 100%;
  }
  .band { fill: var(--sky); }
  .brand {
    position: absolute;
    left: 64px;
    top: 112px;
    display: flex;
    align-items: center;
    gap: 14px;
  }
  .brand-mark {
    width: 22px;
    height: 22px;
    background: var(--silver);
  }
  .brand-name {
    font-family: "Nunito Sans", sans-serif;
    font-weight: 600;
    font-size: 30px;
    line-height: 1.05;
    letter-spacing: 0.5px;
    color: var(--silver);
  }
  .card-back {
    display: flex;
    align-items: center;
    justify-content: center;
    gap: 20px;
  }
  .identity {
    text-align: right;
  }
  .person-name {
    font-family: "Oswald", sans-serif;
    font-weight: 600;
    font-size: 30px;
    letter-spacing: 1px;
    color: var(--sky);
    text-transform: uppercase;
    line-height: 1.05;
  }
  .person-role {
    font-family: "Nunito Sans", sans-serif;
    font-size: 14px;
    color: var(--white);
    margin-top: 2px;
  }
  .divider {
    width: 2px;
    height: 58px;
    background: var(--gold);
  }
  .contacts {
    list-style: none;
    font-family: "Nunito Sans", sans-serif;
    color: var(--white);
  }
  .contact {
    display: flex;
    align-items: center;
    gap: 8px;
  }
  .contact-phone { font-size: 19px; }
  .contact-email { font-size: 13px; margin-top: 4px; }
  .contact svg { fill: var(--sky); flex: none; }
</style>
</head>
<body>
  <main class="sheet">
    <section class="card card-front" aria-label="Card front">
      <svg class="bands" viewBox="0 0 560 320" preserveAspectRatio="none" aria-hidden="true">
        <polygon class="band" points="0,0 210,0 180,26 0,26"/>
        <polygon class="band" points="0,62 470,62 420,106 0,106"/>
        <polygon class="band" points="0,150 400,150 345,196 0,196"/>
        <polygon class="band" points="0,240 520,240 470,284 0,284"/>
      </svg>
      <div class="brand">
        <span class="brand-mark"></span>
        <span class="brand-name">Copperleaf<br>Motorized Shade</span>
      </div>
    </section>

    <section class="card card-back" aria-label="Card back">
      <div class="identity">
        <p class="person-name">Daniel Reyes</p>
        <p class="person-role">President</p>
      </div>
      <span class="divider"></span>
      <ul class="contacts">
        <li class="contact contact-phone">
          <svg width="12" height="14" viewBox="0 0 24 24" aria-hidden="true"><path d="M6.6 10.8a15.1 15.1 0 0 0 6.6 6.6l2.2-2.2a1 1 0 0 1 1-.25 11.4 11.4 0 0 0 3.6.57 1 1 0 0 1 1 1V20a1 1 0 0 1-1 1A17 17 0 0 1 3 4a1 1 0 0 1 1-1h3.5a1 1 0 0 1 1 1c0 1.25.2 2.45.57 3.57a1 1 0 0 1-.25 1z"/></svg>
          (555) 014-2380
        </li>
        <li class="contact contact-email">
          <svg width="14" height="10" viewBox="0 0 24 17" aria-hidden="true"><path d="M0 0h24v17H0z M1.5 1.5 12 9.5 22.5 1.5" fill="var(--sky)"/><path d="M1.5 1.5 12 9.5 22.5 1.5" fill="none" stroke="var(--navy)" stroke-width="1.6"/></svg>
          d.reyes@mailbox.com
        </li>
      </ul>
    </section>
  </main>
</body>
</html>
```